CG 1 page flyer

I need a flyer design for a financial risk advisory business. I like the layout of the example on your site, for Delia Fenwick (attached). Our business needs to show strength, safety, knowledge and security. We provide financial advice.

I have uploaded the front page of our larger brochure. I would like the man with the umbrella with the caption and the logo / brand on the front page, but with portrait orientation, instead of landscape.

For the second page (the back), I have got some ideas of the kinds of things I would want written on the attached Power Point. But it needs to be arranged better, with perhaps the Corvin's Gate Logo on there as well, to break up all the writing. Attached is an example of how it might look, but I want different formatting and layout ideas, that look better, more professional etc.

The page 1 comment what is corvins gate? predicting ......... would look better all the way along the bottom of the page, but i couldn't get the formatting right.

```html
<!DOCTYPE html>
<html lang="en">
<head>
<meta charset="utf-8">
<title>Corvin's Gate — Flyer</title>
<link href="https://fonts.googleapis.com/css2?family=Lato:wght@300;400;700;900&display=swap" rel="stylesheet">
<style>
  :root {
    --backdrop: #e6e6e4;
    --paper: #ffffff;
    --navy: #252a5e;
    --sky: #1aa3dc;
    --ink: #1b1b1b;
    --mist-top: #f4f5f5;
    --mist-bottom: #c9cacc;
    --storm-1: #1c2430;
    --storm-2: #3c4c60;
    --storm-3: #56667a;
  }
  * { margin: 0; padding: 0; box-sizing: border-box; }
  html, body { width: 1200px; height: 960px; overflow: hidden; }
  body {
    background: var(--backdrop);
    font-family: "Lato", Arial, sans-serif;
    color: var(--ink);
    position: relative;
  }
  .flyer {
    position: absolute;
    left: 280px; top: 27px;
    width: 640px; height: 905px;
    background: var(--paper);
    overflow: hidden;
    box-shadow: 0 2px 10px rgba(0,0,0,.18);
  }
  .hero {
    position: absolute;
    left: 0; top: 41px; width: 640px; height: 198px;
    background:
      radial-gradient(ellipse at 62% 55%, var(--storm-3) 0%, transparent 55%),
      linear-gradient(180deg, var(--storm-1) 0%, var(--storm-2) 60%, var(--storm-1) 100%);
  }
  .hero-line {
    position: absolute;
    font-weight: 300;
    font-size: 23px;
    letter-spacing: .5px;
    line-height: 1;
  }
  .hero-left { color: #fff; left: 47px; }
  .hero-left strong { font-weight: 700; }
  .hero-right { color: var(--sky); right: 43px; text-align: right; }
  .hero-right.strong { font-weight: 700; font-size: 29px; letter-spacing: 1px; }

  .mist {
    position: absolute;
    left: -19px; top: 235px;
    width: 678px; height: 678px;
    border-radius: 50%;
    background: linear-gradient(180deg, var(--mist-top) 0%, #e2e3e4 50%, var(--mist-bottom) 100%);
  }
  .block {
    position: absolute;
    font-size: 9.6px;
    line-height: 1.36;
    font-weight: 700;
  }
  .block h3 {
    color: var(--sky);
    font-size: 9.6px;
    font-weight: 900;
    text-transform: uppercase;
    letter-spacing: .2px;
  }
  .block h3.sentence { text-transform: none; }
  .block p + h3, .block ul + h3 { margin-top: 9px; }
  .block .underline { text-decoration: underline; }
  .block ul { list-style: none; }
  .block li { position: relative; padding-left: 17px; }
  .block li::before {
    content: ""; position: absolute; left: 5px; top: 4px;
    width: 4px; height: 4px; border-radius: 50%; background: var(--sky);
  }
  .col-left { left: 46px; width: 232px; }
  .col-right { left: 367px; width: 226px; }
  .col-right-low { left: 375px; width: 224px; }

  .brand {
    position: absolute;
    left: 170px; top: 488px;
    width: 300px;
    text-align: center;
    font-size: 28px;
    font-weight: 700;
    color: var(--navy);
    line-height: 1;
  }
  .callout {
    position: absolute;
    left: 64px; top: 750px;
    font-size: 11px; font-weight: 900; line-height: 1.15;
    text-transform: uppercase; letter-spacing: .3px;
  }
  .callout .sky { color: var(--sky); }
  .callout .navy { color: var(--navy); }
</style>
</head>
<body>
  <article class="flyer">
    <div class="hero" role="img" aria-label="Rainy city street at dusk with a figure under an umbrella"></div>
    <div class="hero-line hero-left" style="top:74px">YOU CAN’T OUTSOURCE</div>
    <div class="hero-line hero-left" style="top:108px">YOUR <strong>RISK</strong></div>
    <div class="hero-line hero-right" style="top:124px">BUT</div>
    <div class="hero-line hero-right" style="top:154px">YOU CAN INSOURCE</div>
    <div class="hero-line hero-right strong" style="top:184px">EXPERTISE</div>

    <div class="mist"></div>

    <section class="block col-left" style="top:264px">
      <h3>Who is Corvin’s Gate?</h3>
      <p>A team of independent, passionate risk advisors with over 200 years combined experience in financial market risk management, funding &amp; debt advisory.</p>
      <h3>What can we do for you?</h3>
      <p>We partner with clients to gain a deep understanding of their needs. We then help them <span class="underline">solve their risk and funding issues by creating and explaining sustainable treasury policy.</span></p>
      <h3 class="sentence">Debt Advisory</h3>
      <p>Design &amp; Execution of debt funding strategies.</p>
    </section>

    <section class="block col-right" style="top:264px">
      <h3>What it means for our clients</h3>
      <p>Our market experience means our clients receive well considered, completely independent advice and solutions covering:</p>
      <ul>
        <li>Commodities</li>
        <li>Foreign Exchange</li>
        <li>nterest Rates</li>
        <li>Project Finance</li>
        <li>reasury Software Solutions</li>
        <li>Market Valuations incl. CVA / DVA</li>
        <li>Hedge Effectiveness Testing</li>
        <li>Compliance Reporting</li>
      </ul>
    </section>

    <div class="brand">Corvin’s Gate</div>

    <section class="block col-left" style="top:589px">
      <h3 class="sentence">Market Risk Advisory</h3>
      <p>Design &amp; Execution of hedging strategies</p>
      <h3 class="sentence">Active Engagement</h3>
      <p>Fully engaged risk review, reporting, strategy development and execution enhancement.</p>
      <h3>What is our measure of success?</h3>
      <p>Our only true measure of success is successful, sustainable clients that stand out from their peers.</p>
    </section>

    <div class="callout">
      <span class="sky">Integration of</span><br>
      <span class="navy">Market risk strategy</span><br>
      <span class="navy">&amp; corporate strategy</span><br>
      <span class="sky">is essential</span>
    </div>

    <section class="block col-right-low" style="top:589px">
      <h3>Our principles</h3>
      <ul>
        <li>Aspire to always deliver value to our clients.</li>
        <li>Always provide frank, robust advice.</li>
        <li>Be fierce but commercial client advocates.</li>
      </ul>
      <h3>What’s our philosophy?</h3>
      <p>Markets are dynamic, so proper Risk Management must also be a dynamic and on-going process. Risk Management is not about “beating the market”, its about “not taking a beating” from adverse market conditions.</p>
      <p style="margin-top:12px">When your bottom line is exposed to volatile markets, appropriate preparation is the key to a sustainable business. We help our clients to integrate their risk management objectives with their overall corporate strategy.</p>
    </section>
  </article>
</body>
</html>
```